" Nossa empresa faz atendimentos médicos especializados no tratamento da dor de muito difícil controle sejam estas dores decorrentes de uma cirurgia na coluna, dor do câncer ou qualquer outra. Apartir de uma consulta formulamos modelos de tratamentos com medicamentos associados a técnicas minimamente invasivas para controle das diferentes tipo de dor que os pacientes nos trazem. Somos especialistas em tratamento de dor e utilizamos além de atendimento clínico diversas técnicas de cirurgias modernas para alívio da dor do paciente Uma das técnicas mais modernas e utilizadas são as técnicas de neuromodulação da dor onde atravéz de microchips ou micro eletrodos implantados no corpo do paciente conseguimos bloquear os estímulos neurológicos que levam a informação de dor Fazemos também muito procedimentos chamados minimamente invasivos onde através destas técnicas com mínimo agressão conseguimos alivar as dores dos pacientes "

```html
<!DOCTYPE html>
<html lang="pt-BR">
<head>
<meta charset="utf-8">
<title>Clínica Alívio Pleno – Pasta</title>
<link href="https://fonts.googleapis.com/css2?family=Montserrat:wght@400;600;700&display=swap" rel="stylesheet">
<style>
  :root {
    --bg: #eceeef;
    --brand-blue: #1c4fd0;
    --brand-navy: #1d3f9a;
    --paper: #ffffff;
    --mist: #e6e7e9;
    --ink-light: #ffffff;
  }
  html, body {
    margin: 0;
    padding: 0;
    width: 1200px;
    height: 1200px;
    overflow: hidden;
    background: var(--bg);
    font-family: "Montserrat", Arial, sans-serif;
  }
  .folder {
    position: absolute;
    left: 216px;
    top: 233px;
    width: 792px;
    height: 740px;
  }
  .folder-back {
    position: absolute;
    left: 0;
    top: 0;
    width: 396px;
    height: 740px;
  }
  .folder-back svg { display: block; }
  .folder-front {
    position: absolute;
    left: 396px;
    top: 0;
    width: 396px;
    height: 740px;
    background: var(--paper);
    overflow: hidden;
    box-shadow: 0 2px 6px rgba(0,0,0,0.08);
  }
  .decor-ring {
    position: absolute;
    left: 40px;
    top: 190px;
    width: 300px;
    height: 300px;
    border-radius: 50%;
    border: 26px solid var(--mist);
    box-sizing: border-box;
  }
  .front-brand {
    position: absolute;
    left: 62px;
    top: 250px;
    display: flex;
    align-items: center;
    gap: 12px;
    background: var(--paper);
    padding: 10px 8px;
  }
  .front-brand .dot {
    width: 34px;
    height: 34px;
    border-radius: 50%;
    background: var(--brand-navy);
    flex: none;
  }
  .front-brand .name {
    color: var(--brand-navy);
    font-weight: 700;
    font-size: 26px;
    line-height: 1.05;
    text-transform: uppercase;
  }
  .back-content {
    position: absolute;
    left: 130px;
    top: 340px;
    width: 220px;
    color: var(--ink-light);
  }
  .back-brand {
    display: flex;
    align-items: center;
    gap: 8px;
    margin-left: 30px;
    margin-bottom: 30px;
  }
  .back-brand .dot {
    width: 22px;
    height: 22px;
    border-radius: 50%;
    background: var(--ink-light);
    flex: none;
  }
  .back-brand .name {
    font-weight: 700;
    font-size: 14px;
    line-height: 1.1;
    text-transform: uppercase;
  }
  .booking-title {
    font-weight: 700;
    font-size: 10px;
    margin: 0 0 3px 28px;
    letter-spacing: 0.2px;
  }
  .contact-row {
    display: flex;
    align-items: flex-start;
    gap: 8px;
    font-size: 9px;
    line-height: 1.35;
    margin-bottom: 9px;
  }
  .contact-row svg { flex: none; margin-top: 1px; }
  .contact-row .phones { font-weight: 700; }
</style>
</head>
<body>
  <div class="folder">
    <div class="folder-back">
      <svg width="396" height="740" viewBox="0 0 396 740" aria-hidden="true">
        <path d="M0 0 H396 V740 H260 C170 740 110 700 80 640 C60 600 40 560 0 540 Z" fill="var(--brand-blue)"/>
      </svg>
      <div class="back-content">
        <div class="back-brand">
          <span class="dot"></span>
          <span class="name">Clínica<br>Alívio Pleno</span>
        </div>
        <p class="booking-title">CENTRAL DE MARCAÇÕES</p>
        <div class="contact-row">
          <svg width="14" height="14" viewBox="0 0 14 14" aria-hidden="true"><path d="M3 1 L5 1 L6 4 L4.5 5 C5.3 7 7 8.7 9 9.5 L10 8 L13 9 L13 11 C13 12 12 13 11 13 C5.5 13 1 8.5 1 3 C1 2 2 1 3 1 Z" fill="var(--ink-light)"/></svg>
          <span class="phones">00 0000 0000<br>00 0000 0000</span>
        </div>
        <div class="contact-row">
          <svg width="14" height="14" viewBox="0 0 14 14" aria-hidden="true"><path d="M7 1 C4.5 1 3 2.8 3 5 C3 8 7 13 7 13 C7 13 11 8 11 5 C11 2.8 9.5 1 7 1 Z" fill="var(--ink-light)"/><circle cx="7" cy="5" r="1.5" fill="var(--brand-blue)"/></svg>
          <span>Rua das Acácias, 0000 -<br>00000-000 Centro / UF / Brasil</span>
        </div>
        <div class="contact-row">
          <svg width="14" height="14" viewBox="0 0 14 14" aria-hidden="true"><rect x="1" y="3" width="12" height="8" rx="1" fill="var(--ink-light)"/><path d="M1.5 3.5 L7 8 L12.5 3.5" fill="none" stroke="var(--brand-blue)" stroke-width="1"/></svg>
          <span>contato@aliviopleno.com.br<br><strong>www.aliviopleno.com.br</strong></span>
        </div>
      </div>
    </div>
    <div class="folder-front">
      <div class="decor-ring"></div>
      <div class="front-brand">
        <span class="dot"></span>
        <span class="name">Clínica<br>Alívio Pleno</span>
      </div>
    </div>
  </div>
</body>
</html>
```